Post Card Mailer for QUIK PATH PROSPECTS using new logo

We need a post card designed to send through the USA mail service that will go to new prospective clients.

The post card will introduce me and my new company and try to educate them our on company and services.

The goal is for them to call me or email me so I can have a discussion and try to sell our product.

Our product is a name list of individuals that are looking for consulting / help to determine if they qualify for USA social security benefits and then help to manage the process. We sell this name list to law firms that help these individuals.

Our services are better because we have a better less expensive way to identify people via the internet that want help. Our conversion rate is 15%, so every 100 leads a law firm buys the will obtain 15 customers / clients.

Designer on Logo took alot longer than expected. Also there were two projects that needed to combined into one. Which was done yesterday.

Target Market(s)

Law firms

Font styles to use
Serif
Sans Serif
Script

Colors

Designer to choose colors to be used in the design.

Requirements
Must have
• The size of the mailer should be about 6 by 8 inches.
• Two sides.
• Side 1: With our Logo and key messages we want to communicate.
• Side 2: A space to be used by the USA mail services in lower right, my photo and an introduction by me to our company and why they should buy from my company.
Nice to have
• Images that represent what we do, how we help, and our target market.
Should not have
• Poor taste in images that upset people

```html
<!DOCTYPE html>
<html lang="en">
<head>
<meta charset="utf-8">
<title>Quik Path Prospects – Postcard Mailer</title>
<link rel="stylesheet" href="https://fonts.googleapis.com/css2?family=Open+Sans:wght@400;600;700;800&family=Libre+Baskerville:wght@400&display=swap">
<style>
  :root{
    --bg:#e9e9ea;
    --card:#ffffff;
    --blue:#1c6fc4;
    --blue-dark:#135aa3;
    --ink:#4a4b4d;
    --muted:#7c7d80;
    --band:#a9aaad;
    --band-dark:#8e8f92;
    --rule:#c9cacc;
  }
  *{box-sizing:border-box;margin:0;padding:0}
  html,body{width:1200px;height:900px;overflow:hidden}
  body{background:var(--bg);font-family:"Open Sans",Arial,sans-serif;color:var(--ink);position:relative}
  .card{position:absolute;width:560px;height:420px;background:var(--card);overflow:hidden;box-shadow:0 6px 18px rgba(0,0,0,.18)}
  .card--front{left:40px;top:40px}
  .card--back{left:600px;top:440px}
  .card__shapes{position:absolute;inset:0}
  .wordmark{font-family:"Open Sans",Arial,sans-serif;font-weight:800;color:var(--blue);letter-spacing:.02em;display:flex;align-items:center;gap:6px;line-height:1;white-space:nowrap}
  .wordmark__dot{width:9px;height:9px;background:var(--blue);flex:none}

  /* front */
  .front__logo{position:absolute;left:22px;top:132px;font-size:13px}
  .front__points{position:absolute;left:22px;top:160px;width:180px}
  .point__title{font-size:10.5px;font-weight:700;color:var(--blue);margin-top:7px}
  .point__list{list-style:none;font-size:8.6px;line-height:1.3;color:var(--ink)}
  .point__list li::before{content:"• "}
  .front__band{position:absolute;left:0;bottom:0;width:100%;height:60px;background:var(--band);display:flex;align-items:center;padding-left:22px;gap:10px;color:#fff;font-size:11px}
  .globe{width:20px;height:20px}

  /* back */
  .portrait{position:absolute;left:18px;top:88px;width:56px;height:64px;background:linear-gradient(160deg,#3c5f8c,#22354f);border:2px solid #fff;box-shadow:0 0 0 1px var(--rule)}
  .sender__name{position:absolute;left:84px;top:92px;font-family:"Libre Baskerville",Georgia,serif;font-size:15px;color:var(--ink)}
  .sender__role{position:absolute;left:84px;top:116px;font-family:"Libre Baskerville",Georgia,serif;font-size:9px;color:var(--muted)}
  .intro{position:absolute;left:18px;top:166px;width:200px;font-size:7.6px;line-height:1.35;color:var(--ink)}
  .intro__lead{font-family:"Libre Baskerville",Georgia,serif;font-size:8px;margin-bottom:6px}
  .intro__list{list-style:none}
  .intro__list li{margin-bottom:6px;padding-left:9px;position:relative}
  .intro__list li::before{content:"•";position:absolute;left:0}
  .back__logo{position:absolute;left:300px;top:26px;font-size:13px}
  .offer{position:absolute;left:300px;top:60px;width:150px;font-size:7.4px;line-height:1.35;color:var(--ink)}
  .offer__title{font-size:10px;font-weight:700;color:var(--blue);margin:7px 0 3px}
  .offer__list{list-style:none}
  .offer__list li::before{content:"• "}
  .stamp{position:absolute;right:22px;top:62px;width:52px;height:58px;border:1px solid var(--rule)}
  .address{position:absolute;left:300px;top:168px;font-size:6.4px;line-height:1.4;color:var(--muted)}
  .address-lines{position:absolute;left:395px;top:176px;width:140px}
  .address-lines span{display:block;height:1px;background:var(--rule);margin-bottom:15px}
  .back__band{position:absolute;left:0;bottom:0;width:100%;height:28px;background:var(--band);color:#fff;font-size:7.6px;font-style:italic;display:flex;align-items:center;padding-left:18px}
</style>
</head>
<body>

<section class="card card--front" aria-label="Postcard front">
  <svg class="card__shapes" width="560" height="420" viewBox="0 0 560 420">
    <defs>
      <linearGradient id="statueTone" x1="0" y1="0" x2="1" y2="0">
        <stop offset="0" stop-color="#dcdbd9"/>
        <stop offset=".45" stop-color="#8f8378"/>
        <stop offset=".7" stop-color="#5b4a3d"/>
        <stop offset="1" stop-color="#cfcdca"/>
      </linearGradient>
      <linearGradient id="scaleTone" x1="0" y1="0" x2="0" y2="1">
        <stop offset="0" stop-color="#ffffff" stop-opacity="0"/>
        <stop offset="1" stop-color="#d9d9db"/>
      </linearGradient>
    </defs>
    <rect x="0" y="180" width="220" height="180" fill="url(#scaleTone)" role="img" aria-label="Faint scales of justice"/>
    <polygon points="188,0 560,0 560,360 280,360 228,210 196,40" fill="url(#statueTone)" role="img" aria-label="Bronze statue of Lady Justice holding scales"/>
    <polyline points="282,364 228,210 196,40" fill="none" stroke="var(--blue)" stroke-width="11" stroke-linejoin="miter"/>
    <polygon points="190.8,10 211,38 181,43.5" fill="var(--blue)"/>
  </svg>

  <div class="wordmark front__logo"><span class="wordmark__dot"></span>QUIK PATH PROSPECTS</div>

  <div class="front__points">
    <p class="point__title">Best Leads, Best Price</p>
    <ul class="point__list">
      <li>Our high conversion rates lower your client acquisition cost</li>
      <li>Referrals available</li>
    </ul>
    <p class="point__title">High Volume, Quality Leads</p>
    <ul class="point__list">
      <li>30 years of SSD domain knowledge</li>
      <li>Tested technology capabilities</li>
    </ul>
    <p class="point__title">Trusted Partner</p>
    <ul class="point__list">
      <li>Reliable, dependable, helpful</li>
      <li>Deep business &amp; process acumen</li>
    </ul>
    <p class="point__title">Quick to use</p>
    <ul class="point__list">
      <li>Integrate seamlessly into your IT systems</li>
      <li>Tailored campaigns</li>
    </ul>
  </div>

  <div class="front__band">
    <svg class="globe" viewBox="0 0 20 20" aria-hidden="true">
      <circle cx="10" cy="10" r="9" fill="var(--band-dark)"/>
      <g fill="none" stroke="#fff" stroke-width="1.1">
        <circle cx="10" cy="10" r="6"/>
        <ellipse cx="10" cy="10" rx="2.6" ry="6"/>
        <line x1="4" y1="10" x2="16" y2="10"/>
      </g>
    </svg>
    <span class="web">www.quikpathprospects.com</span>
  </div>
</section>

<section class="card card--back" aria-label="Postcard back">
  <svg class="card__shapes" width="560" height="420" viewBox="0 0 560 420">
    <defs>
      <linearGradient id="gavelTone" x1="0" y1="0" x2="1" y2="1">
        <stop offset="0" stop-color="#ffffff" stop-opacity="0"/>
        <stop offset="1" stop-color="#cfcfd1"/>
      </linearGradient>
    </defs>
    <rect x="380" y="250" width="180" height="142" fill="url(#gavelTone)" role="img" aria-label="Faint judge's gavel"/>
    <polyline points="262,392 228,255 262,130 262,30" fill="none" stroke="var(--blue)" stroke-width="9"/>
    <polygon points="262,4 276,32 248,32" fill="var(--blue)"/>
  </svg>

  <div class="portrait" role="img" aria-label="Portrait photo of the company president"></div>
  <p class="sender__name">Mason Treadwell</p>
  <p class="sender__role">(President, Quik Path Prospects)</p>

  <div class="intro">
    <p class="intro__lead">I want to Personally Introduce our Company to you!</p>
    <ul class="intro__list">
      <li>My team w/ 30 years of cumulative SSD experience.</li>
      <li>We have proven technology that delivers the best leads.</li>
      <li>The timing is right for a new competitor in this industry.</li>
      <li>I had to come out of retirement after 10 years with SSD. The opportunity is just that great… and I love building businesses and partnering with businesses.</li>
      <li>Our business, industry &amp; technical acumen is unrivaled… and we can do it at a cost that no others can.</li>
    </ul>
  </div>

  <div class="wordmark back__logo"><span class="wordmark__dot"></span>QUIK PATH PROSPECTS</div>

  <div class="offer">
    <p>Best Leads… Best Price with High Volume &amp; Quality capacity… Leads from a Trusted Partner that is Quick to use</p>
    <p class="offer__title">Test our Leads</p>
    <ul class="offer__list">
      <li>Start at 250 or 500 Leads</li>
      <li>Grow to 1,000 … 5,000 or even 10,000</li>
      <li>We give the right support to your growth.</li>
    </ul>
  </div>

  <div class="stamp" aria-label="Postage area"></div>

  <address class="address">
    Quik Path Prospects<br>
    410 Harbor Lane Suite 2<br>
    Austin, TX 78701<br>
    (512) 555-0147<br>
    hello@quikpathprospects.com
  </address>
  <div class="address-lines" aria-hidden="true"><span></span><span></span><span></span><span></span></div>

  <div class="back__band">Let's work together to bring Social Security Disability benefits to those in need and deserving!</div>
</section>

</body>
</html>
```